PowerPoint Template

We would like new powerpoint template for our organization: Fjordvik Data Guild.
Enclosed you find our logo and old template.
Industry/Entity Type
Computer
Requirements
Must have
- 1. Logo
2. Footer (for autor)
3. Font: Variations of ARIAL

```html
<!DOCTYPE html>
<html lang="no">
<head>
<meta charset="utf-8">
<title>Fjordvik Data Guild – PowerPoint-mal</title>
<link href="https://fonts.googleapis.com/css2?family=Arimo:wght@400;700&display=swap" rel="stylesheet">
<style>
  :root{
    --bg-top:#dcdcfb;
    --bg-bottom:#ffffff;
    --slide:#efefef;
    --slide-end:#d9d9d9;
    --brand-blue:#3a6db1;
    --brand-blue-dark:#22467a;
    --accent-teal:#5b9db3;
    --footer:#6e6f71;
    --text:#8a8a8a;
    --title-dark:#2a2a2a;
    --white:#ffffff;
  }
  *{margin:0;padding:0;box-sizing:border-box}
  html,body{width:800px;height:1200px;overflow:hidden}
  body{
    position:relative;
    background:linear-gradient(180deg,var(--bg-top) 0%,#f1eef8 40%,var(--bg-bottom) 70%);
    font-family:"Arimo",Arial,sans-serif;
  }

  /* Cover slide */
  .cover{position:absolute;left:185px;top:62px;width:430px;height:238px;overflow:hidden}
  .cover-photo{
    position:absolute;inset:0;
    background:linear-gradient(100deg,#cfd2d3 0%,#e6e2dc 35%,#9a9b9c 60%,#4c4d50 80%,#8e8f91 100%);
  }
  .cover-brand{
    position:absolute;right:14px;top:22px;display:flex;align-items:center;gap:5px;
    font-size:11px;color:var(--title-dark);
  }
  .cover-brand .dot{width:14px;height:14px;border-radius:50%;background:var(--brand-blue)}
  .cover-title{position:absolute;left:38px;top:198px;font-size:12px;font-weight:400;color:var(--title-dark)}
  .cover-date{position:absolute;left:92px;top:215px;font-size:5px;color:var(--title-dark)}

  /* Content slides */
  .slide{position:absolute;width:328px;height:238px;background:var(--slide);overflow:hidden}
  .slide-1{left:45px;top:530px}
  .slide-2{left:427px;top:530px}
  .slide-3{left:45px;top:802px}
  .slide-4{left:427px;top:802px;background:var(--slide-end)}

  .top-band{position:absolute;left:0;top:18px}
  .slide-title{position:absolute;left:20px;top:40px;font-size:18px;color:var(--brand-blue);font-weight:400}

  .footer{
    position:absolute;left:0;bottom:0;width:100%;height:24px;background:var(--footer);
    display:flex;align-items:center;justify-content:space-between;padding:0 20px;
    color:var(--white);font-size:4px;letter-spacing:.2px;
  }
  .footer-brand{display:flex;align-items:center;gap:3px;font-size:4.5px}
  .footer-brand .mark{width:8px;height:8px;background:var(--brand-blue)}
  .footer-meta{text-transform:uppercase}
  .footer-meta span{margin-left:10px}

  .pillars{position:absolute;left:20px;top:98px;display:flex;gap:10px}
  .pillar{
    width:64px;height:64px;border-radius:50%;display:flex;align-items:center;justify-content:center;
    text-align:center;color:var(--white);font-size:5.5px;line-height:1.25;padding:0 6px;
  }
  .pillar-events{background:radial-gradient(circle at 50% 40%,#b8574e,#8f1f24)}
  .pillar-members{background:radial-gradient(circle at 40% 40%,#e8c2a8,#b98166)}
  .pillar-social{background:radial-gradient(circle at 40% 35%,#7fb3e0,#1f4f86)}
  .pillar-brand{background:radial-gradient(circle at 50% 50%,#c9a070,#a0603e 55%,#6d7d52)}

  .columns{position:absolute;left:20px;top:71px;width:288px;display:flex;gap:8px}
  .column{flex:1;font-size:4px;line-height:5.3px;color:var(--text)}
  .column p{margin-bottom:3px}

  .contact{position:absolute;left:20px;top:70px;font-size:4.6px;line-height:9px;color:var(--text)}
  .map{
    position:absolute;left:168px;top:53px;width:135px;height:135px;border-radius:50%;
    background:radial-gradient(circle at 45% 45%,#f1ede4,#dcd8cf 70%,#cfcbc2);
  }

  .end-brand{
    position:absolute;right:24px;top:30px;display:flex;align-items:center;gap:4px;
    font-size:6px;color:var(--title-dark);
  }
  .end-brand .mark{width:10px;height:10px;background:var(--brand-blue)}
  .closing-art{
    position:absolute;left:94px;top:60px;width:136px;height:114px;
    background:linear-gradient(160deg,var(--brand-blue) 0%,var(--accent-teal) 100%);
    opacity:.85;
  }
  .closing-word{
    position:absolute;left:94px;top:110px;width:136px;text-align:center;
    font-size:5px;color:var(--white);letter-spacing:.3px;
  }
</style>
</head>
<body>

  <!-- Cover -->
  <section class="cover">
    <div class="cover-photo" role="img" aria-label="Photo of a businesswoman with a laptop and phone seated in an airport lounge"></div>
    <div class="cover-brand"><span class="dot"></span>fjordvikdata.no</div>
    <h1 class="cover-title">Fjordvik Data Guild</h1>
    <p class="cover-date">Januar 2014</p>
  </section>

  <!-- Slide 1 -->
  <section class="slide slide-1">
    <svg class="top-band" width="306" height="16" viewBox="0 0 306 16" aria-hidden="true">
      <polygon points="0,0 302,0 306,12 0,12" fill="var(--brand-blue)"/>
      <polygon points="298,12 306,12 302,16" fill="var(--brand-blue-dark)"/>
    </svg>
    <h2 class="slide-title">Hva gjør vi?</h2>
    <div class="pillars">
      <div class="pillar pillar-events" role="img" aria-label="Photo of a crowd at an event">Markedsfører arrangementer</div>
      <div class="pillar pillar-members" role="img" aria-label="Photo of a member">Bidrar til å verve medlemmer</div>
      <div class="pillar pillar-social" role="img" aria-label="Photo of blue bubbles">Skaper synlighet i Sosiale Medier</div>
      <div class="pillar pillar-brand" role="img" aria-label="Photo of coloured pencils">Bygger merkevare og omdømme</div>
    </div>
    <footer class="footer">
      <div class="footer-brand"><span class="mark"></span>Fjordvik</div>
      <div class="footer-meta">Fjordvik Data Guild<span>1</span></div>
    </footer>
  </section>

  <!-- Slide 2 -->
  <section class="slide slide-2">
    <svg class="top-band" width="306" height="16" viewBox="0 0 306 16" aria-hidden="true">
      <polygon points="0,0 302,0 306,12 0,12" fill="var(--brand-blue)"/>
      <polygon points="298,12 306,12 302,16" fill="var(--brand-blue-dark)"/>
    </svg>
    <h2 class="slide-title">Hva gjør vi?</h2>
    <div class="columns">
      <div class="column">
        <p>Vi samler fagfolk innen IT og gir medlemmer faglige møteplasser, kurs og nettverk gjennom hele året i hele landet.</p>
        <p>Foreningen arbeider for kompetanse, etikk og god bruk av teknologi i arbeidsliv, skole og samfunn.</p>
        <p>Faggruppene arrangerer seminarer og konferanser der medlemmer deler erfaring og lærer av hverandre.</p>
        <p>Vi gir ut fagblad og nyhetsbrev.</p>
      </div>
      <div class="column">
        <p>Medlemskap gir rabatt på kurs, tilgang til faggrupper og et sterkt nettverk av engasjerte kolleger over hele landet.</p>
        <p>Studenter og nyutdannede får egne tilbud som gjør overgangen til arbeidslivet enklere.</p>
        <p>Vi samarbeider med næringsliv, skoler og myndigheter om digital kompetanse.</p>
        <p>Les mer på nettsiden vår.</p>
      </div>
    </div>
    <footer class="footer">
      <div class="footer-brand"><span class="mark"></span>Fjordvik</div>
      <div class="footer-meta">Fjordvik Data Guild<span>2</span></div>
    </footer>
  </section>

  <!-- Slide 3 -->
  <section class="slide slide-3">
    <svg class="top-band" width="306" height="16" viewBox="0 0 306 16" aria-hidden="true">
      <polygon points="0,0 302,0 306,12 0,12" fill="var(--brand-blue)"/>
      <polygon points="298,12 306,12 302,16" fill="var(--brand-blue-dark)"/>
    </svg>
    <h2 class="slide-title">Fjordvik Data Guild</h2>
    <div class="contact">
      Post- og besøksadresse: Strandveien 12, 0150 Fjordvik<br>
      Telefon: 22 90 14 70<br>
      Telefaks: 22 90 14 71<br>
      E-post: post@fjordvikdata.no
    </div>
    <div class="map" role="img" aria-label="Street map showing the office location"></div>
    <footer class="footer">
      <div class="footer-brand"><span class="mark"></span>Fjordvik</div>
      <div class="footer-meta">Fjordvik Data Guild<span>3</span></div>
    </footer>
  </section>

  <!-- Slide 4 -->
  <section class="slide slide-4">
    <div class="end-brand"><span class="mark"></span>fjordvikdata.no</div>
    <div class="closing-art" role="img" aria-label="Decorative blue banner graphic for the closing message"></div>
    <p class="closing-word">TAKK</p>
  </section>

</body>
</html>
```